Packaging Design for Boneless Picnic Ham

We are Tidewell Provisions Limited, a company based in Trinidad which is located within the Caribbean. We produce and sell a plethora of meat products including a variety of hams, sausages and even bacon.

We require a packaging design for a ham product. This product is packaged within a cryovac (11" X 18") shrink bag which would be used to package our Boneless Picnic Ham which weighs 2.5 Kilograms.

The design space should be 7 inches wide and 6 inches in height. The design is 3 inches from the bottom and 2 inches off each side.

Our target audience comprises of caterers as well as the average household folk. What sets our product apart is that it is has a great taste, 20% less salt and is affordable and easy. We commonly refer to it as the "Sunday Roast Joint".

Attached below, is our logo which you must incorporate onto the design. We also request that the header be "Hickory Smoked Boneless Picnic Ham".

Target Market(s)

Caterers and Average Household Folk

Font styles to use
Sans Serif

Requirements
Must have
• The Tidewell Provisions Company Logo and the header must have "Hickory Smoked Boneless Picnic Ham"
Nice to have
• Maximum Creativity
Should not have
• No animal artwork should be included onto the design

```html
<!DOCTYPE html>
<html lang="en">
<head>
<meta charset="utf-8">
<title>Tidewell Provisions – Boneless Picnic Ham Label</title>
<link href="https://fonts.googleapis.com/css2?family=Oswald:wght@300;500;600&family=Cinzel:wght@600&family=Playfair+Display:ital,wght@1,600&display=swap" rel="stylesheet">
<style>
  :root {
    --page-bg: #f6f6f6;
    --label-black: #151515;
    --gold-light: #f7e08a;
    --gold: #d9a227;
    --gold-deep: #a87512;
    --ham-red: #b0061f;
    --ham-red-dark: #6a0008;
    --navy: #141a6e;
    --text-silver: #e9e6de;
    --text-white: #ffffff;
  }
  * { margin: 0; padding: 0; box-sizing: border-box; }
  html, body { width: 1200px; height: 1200px; overflow: hidden; background: var(--page-bg); }
  .label { position: relative; width: 1200px; height: 1200px; }
  .label-shapes { position: absolute; inset: 0; }
  .text { position: absolute; left: 0; width: 1200px; text-align: center; }
  .brand-name {
    top: 206px; left: 464px; width: 290px;
    font-family: "Oswald", sans-serif; font-weight: 600;
    font-size: 44px; line-height: 1.05; color: var(--text-white);
    letter-spacing: 1px; text-transform: uppercase;
  }
  .product-line-1 {
    top: 418px; left: 350px; width: 520px;
    font-family: "Oswald", sans-serif; font-weight: 300;
    font-size: 104px; line-height: 1; color: var(--text-silver);
    letter-spacing: -1px;
  }
  .product-line-2 {
    top: 506px; left: 350px; width: 520px;
    font-family: "Oswald", sans-serif; font-weight: 600;
    font-size: 104px; line-height: 1; color: var(--text-silver);
    letter-spacing: -1px;
  }
  .variant {
    top: 627px; left: 324px; width: 568px;
    font-family: "Cinzel", serif; font-weight: 600;
    font-size: 46px; line-height: 1; color: var(--gold);
    letter-spacing: 2px;
  }
  .quality-mark {
    top: 732px; left: 556px; width: 84px;
    font-family: "Playfair Display", serif; font-style: italic; font-weight: 600;
    font-size: 17px; line-height: 1.05; color: var(--gold);
    transform: rotate(-14deg);
  }
  .weight-box {
    top: 826px; left: 536px; width: 128px;
    font-family: "Oswald", sans-serif; font-weight: 500; color: var(--text-white);
    line-height: 1;
  }
  .weight-box .weight-label { font-size: 32px; display: block; }
  .weight-box .weight-value { font-size: 76px; color: var(--gold); display: block; font-weight: 600; margin-top: 2px; }
  .weight-box .weight-unit { font-size: 20px; display: block; margin-top: 2px; }
</style>
</head>
<body>
<div class="label">
  <svg class="label-shapes" width="1200" height="1200" viewBox="0 0 1200 1200" aria-hidden="false">
    <defs>
      <linearGradient id="gold-rim" x1="0" y1="0" x2="1" y2="1">
        <stop offset="0" stop-color="var(--gold-light)"/>
        <stop offset="0.35" stop-color="var(--gold)"/>
        <stop offset="0.7" stop-color="var(--gold-light)"/>
        <stop offset="1" stop-color="var(--gold-deep)"/>
      </linearGradient>
      <radialGradient id="inner-bg" cx="0.5" cy="0.55" r="0.6">
        <stop offset="0" stop-color="#2a2a2a"/>
        <stop offset="1" stop-color="var(--label-black)"/>
      </radialGradient>
      <linearGradient id="red-tab" x1="0" y1="0" x2="0" y2="1">
        <stop offset="0" stop-color="var(--ham-red)"/>
        <stop offset="1" stop-color="var(--ham-red-dark)"/>
      </linearGradient>
      <linearGradient id="ribbon-red" x1="0" y1="0" x2="1" y2="0">
        <stop offset="0" stop-color="var(--ham-red-dark)"/>
        <stop offset="0.5" stop-color="#8a0010"/>
        <stop offset="1" stop-color="var(--ham-red-dark)"/>
      </linearGradient>
      <linearGradient id="tail-red" x1="0" y1="0" x2="1" y2="0">
        <stop offset="0" stop-color="var(--ham-red)"/>
        <stop offset="1" stop-color="var(--ham-red-dark)"/>
      </linearGradient>
      <clipPath id="inner-oval"><ellipse cx="600" cy="552" rx="506" ry="430"/></clipPath>
    </defs>

    <!-- label frame -->
    <ellipse class="rim" cx="600" cy="552" rx="540" ry="462" fill="url(#gold-rim)"/>
    <ellipse class="rim-band" cx="600" cy="552" rx="526" ry="450" fill="var(--label-black)"/>
    <ellipse class="rim-dots" cx="600" cy="552" rx="516" ry="440" fill="none" stroke="var(--gold)" stroke-width="5" stroke-dasharray="8 6"/>
    <ellipse class="inner-field" cx="600" cy="552" rx="506" ry="430" fill="url(#inner-bg)" stroke="var(--gold-light)" stroke-width="2"
      role="img" aria-label="Faint dark photograph of sliced ham behind the product name"/>

    <!-- brand tab -->
    <g clip-path="url(#inner-oval)">
      <rect class="brand-tab" x="464" y="100" width="290" height="316" rx="12" fill="url(#red-tab)" stroke="var(--gold-light)" stroke-width="3"/>
    </g>

    <!-- ribbon tails -->
    <polygon class="ribbon-tail" points="228,648 370,648 370,716 228,716 258,682" fill="url(#tail-red)" stroke="var(--gold-light)" stroke-width="2"/>
    <polygon class="ribbon-tail" points="986,648 844,648 844,716 986,716 956,682" fill="url(#tail-red)" stroke="var(--gold-light)" stroke-width="2"/>
    <polygon class="ribbon-fold" points="324,692 370,716 370,692" fill="#3a0004"/>
    <polygon class="ribbon-fold" points="892,692 844,716 844,692" fill="#3a0004"/>
    <!-- ribbon band -->
    <rect class="ribbon-band" x="324" y="618" width="568" height="74" fill="url(#ribbon-red)" stroke="var(--gold-light)" stroke-width="2"/>

    <!-- quality seal -->
    <circle class="quality-seal" cx="598" cy="756" r="44" fill="#111" stroke="url(#gold-rim)" stroke-width="3"/>

    <!-- weight box -->
    <rect class="weight-panel" x="536" y="816" width="128" height="180" rx="8" fill="var(--navy)" stroke="var(--gold)" stroke-width="2"/>
  </svg>

  <div class="text brand-name">Tidewell<br>Provisions</div>
  <div class="text product-line-1">BONELESS</div>
  <div class="text product-line-2">PICNICHAM</div>
  <div class="text variant">CLASSIC</div>
  <div class="text quality-mark">Quality<br>No.1</div>
  <div class="text weight-box">
    <span class="weight-label">WEIGHS</span>
    <span class="weight-value">2.5</span>
    <span class="weight-unit">KILOGRAMS</span>
  </div>
</div>
</body>
</html>
```